Create a book cover for brindleshelf BPX

We are looking for a designer to design a cover for a log book in two versions. The two versions only have a slight difference in page count and text, other than that, it is one design.

The main color is blue. No black, no white except book title and other text. The cover must closely relate to the interior pages provided in the attachment. The style should be simple and modern, no old school graphics and fonts. Apply color psychology in the design. Please be creative and you are allowed to use download templates and graphic elements, but you must provide commercial licenses.

Here are the basic information of the book:
1. Book title: AUTO SERVICE RECORD JOURNAL
2. Book size: 6x9 inches
3. Page count: 61 (version 1) and 73 (version 2)
4. Platform: brindleshelf bpx

Requirement for version 1:
1. Front cover: book title
2. Spine: no book title and author name
3. Back cover: text on the top and pen name logo on the bottom middle
4. Back cover text:
• Your essential tool for tracking vehicle health and maintenance
• Dedicated sections for maintenance schedules and repair history
• Track up to 30 maintenance schedules and repair history
• Easy-to-use tables and clear layouts
• Perfect for all car owners, from enthusiasts to everyday drivers

We hope it helps you keep your vehicle in excellent condition. Please take a moment to leave a positive review on Brindleshelf and share your experience if you find it helpful. Thank you!

Requirement for version 2:
1. Front cover: book title ,text "COLOR PAGES"
4. Back cover text:
• Track up to 36 maintenance schedules and repair history

Export:
1. Cover design in PDF and editable file format.
2. Sources/Commercial licenses for everything you did not create by yourself including fonts.

```html
<!DOCTYPE html>
<html lang="en">
<head>
<meta charset="utf-8">
<title>Auto Service Record Journal – Front Cover</title>
<link rel="stylesheet" href="https://fonts.googleapis.com/css2?family=Anton&family=Oswald:wght@500&display=swap">
<style>
  :root {
    --page-bg: #f2f3f6;
    --cover-navy: #25357a;
    --cover-highlight: #56628f;
    --ring-blue: #2f4b9f;
    --band-navy: #1f2a5c;
    --road-dark: #1b1b1f;
    --title-white: #ffffff;
    --pill-text: #23347a;
    --icon-fill: #2b3f8c;
    --car-tone-a: #3a3a40;
    --car-tone-b: #0f0f12;
    --logo-dark: #1a2230;
  }
  * { margin: 0; padding: 0; box-sizing: border-box; }
  html, body {
    width: 1200px; height: 1200px; overflow: hidden;
    background: var(--page-bg);
  }
  .stage {
    width: 1200px; height: 1200px;
    display: flex; align-items: center; justify-content: center;
  }
  .front-cover {
    width: 710px; height: 1120px; display: block;
    box-shadow: 0 10px 30px rgba(20, 30, 70, 0.25);
  }
  .title-line {
    font-family: "Anton", "Oswald", sans-serif;
    fill: var(--title-white);
    text-anchor: middle;
  }
  .title-pill-text {
    font-family: "Anton", "Oswald", sans-serif;
    fill: var(--pill-text);
    text-anchor: middle;
  }
  .pen-name {
    font-family: "Oswald", sans-serif;
    font-weight: 500;
    fill: var(--title-white);
    text-anchor: middle;
  }
  .connector { fill: none; stroke: var(--title-white); stroke-width: 3; stroke-dasharray: 14 12; }
</style>
</head>
<body>
<main class="stage">
  <svg class="front-cover" viewBox="0 0 970 1530" xmlns="http://www.w3.org/2000/svg" aria-label="Auto Service Record Journal front cover">
    <defs>
      <linearGradient id="coverGradient" x1="0" y1="0" x2="0.7" y2="0.7">
        <stop offset="0" stop-color="var(--cover-highlight)"/>
        <stop offset="0.45" stop-color="var(--cover-navy)"/>
        <stop offset="1" stop-color="var(--cover-navy)"/>
      </linearGradient>
      <linearGradient id="carGradient" x1="0" y1="0" x2="0" y2="1">
        <stop offset="0" stop-color="var(--car-tone-a)"/>
        <stop offset="1" stop-color="var(--car-tone-b)"/>
      </linearGradient>
      <clipPath id="aboveBand"><rect x="0" y="0" width="970" height="1335"/></clipPath>
    </defs>

    <!-- cover background -->
    <rect class="cover-bg" width="970" height="1530" fill="url(#coverGradient)"/>

    <!-- title -->
    <text class="title-line" x="487" y="222" font-size="158">AUTO</text>
    <text class="title-line" x="487" y="370" font-size="140" textLength="780" lengthAdjust="spacingAndGlyphs">SERVICE RECORD</text>
    <rect class="title-pill" x="287" y="405" width="403" height="115" rx="30" fill="var(--title-white)"/>
    <text class="title-pill-text" x="488" y="496" font-size="82" textLength="320" lengthAdjust="spacingAndGlyphs">JOURNAL</text>

    <!-- hero emblem -->
    <g class="hero-emblem" clip-path="url(#aboveBand)">
      <circle class="emblem-ring" cx="495" cy="1080" r="290" fill="var(--ring-blue)"/>
      <circle class="emblem-disc" cx="495" cy="1080" r="255" fill="var(--title-white)"/>
      <polygon class="road" points="155,1335 825,1335 700,1180 290,1180" fill="var(--road-dark)"/>
      <rect class="road-mark" x="500" y="1285" width="12" height="35" fill="var(--title-white)"/>
      <rect class="car-visual" role="img" aria-label="Front view of a dark sedan on the road"
            x="265" y="905" width="475" height="395" rx="40" fill="url(#carGradient)"/>
    </g>

    <!-- dashed connectors -->
    <path class="connector" d="M148 1058 Q180 960 225 912"/>
    <path class="connector" d="M300 795 Q370 750 428 728"/>
    <path class="connector" d="M572 728 Q630 745 690 785"/>
    <path class="connector" d="M800 895 Q840 960 858 1025"/>

    <!-- service icons -->
    <g class="service-icon" role="img" aria-label="Engine oil can icon">
      <circle cx="500" cy="710" r="72" fill="var(--ring-blue)"/>
      <circle cx="500" cy="710" r="60" fill="var(--title-white)"/>
      <rect x="475" y="680" width="50" height="62" rx="6" fill="var(--icon-fill)"/>
    </g>
    <g class="service-icon" role="img" aria-label="Tire and wheel icon">
      <circle cx="243" cy="840" r="72" fill="var(--ring-blue)"/>
      <circle cx="243" cy="840" r="60" fill="var(--title-white)"/>
      <circle cx="243" cy="840" r="36" fill="none" stroke="var(--icon-fill)" stroke-width="10"/>
      <circle cx="243" cy="840" r="8" fill="var(--icon-fill)"/>
    </g>
    <g class="service-icon" role="img" aria-label="Car battery icon">
      <circle cx="747" cy="833" r="72" fill="var(--ring-blue)"/>
      <circle cx="747" cy="833" r="60" fill="var(--title-white)"/>
      <rect x="714" y="812" width="66" height="44" rx="3" fill="none" stroke="var(--icon-fill)" stroke-width="6"/>
      <rect x="722" y="804" width="12" height="8" fill="var(--icon-fill)"/>
      <rect x="760" y="804" width="12" height="8" fill="var(--icon-fill)"/>
    </g>
    <g class="service-icon" role="img" aria-label="Oil filter icon">
      <circle cx="133" cy="1135" r="72" fill="var(--ring-blue)"/>
      <circle cx="133" cy="1135" r="60" fill="var(--title-white)"/>
      <rect x="107" y="1105" width="52" height="60" rx="5" fill="var(--icon-fill)"/>
    </g>
    <g class="service-icon" role="img" aria-label="Brake disc icon">
      <circle cx="853" cy="1100" r="72" fill="var(--ring-blue)"/>
      <circle cx="853" cy="1100" r="60" fill="var(--title-white)"/>
      <circle cx="853" cy="1100" r="34" fill="none" stroke="var(--icon-fill)" stroke-width="8"/>
      <circle cx="853" cy="1100" r="10" fill="var(--icon-fill)"/>
    </g>

    <!-- bottom band -->
    <rect class="bottom-band" x="0" y="1335" width="970" height="195" fill="var(--band-navy)"/>
    <line class="band-rule" x1="0" y1="1336" x2="970" y2="1322" stroke="var(--ring-blue)" stroke-width="3"/>

    <!-- pen name mark -->
    <g class="pen-name-mark">
      <circle cx="515" cy="1445" r="64" fill="var(--logo-dark)" stroke="var(--title-white)" stroke-width="4"/>
      <text class="pen-name" x="515" y="1455" font-size="27" textLength="104" lengthAdjust="spacingAndGlyphs">LENA VOSKAR</text>
    </g>
  </svg>
</main>
</body>
</html>
```